Banner für Immobilienmakler
Zielgruppe
Immobilienmakler, Immobilienverkauf mit Herz,
Aufgabenstellung
Verkauf von Häusern und Wohnungen, der Banner soll an einen Balkon oder einen Zaun angebracht werden mit dem Hinweis, dass das Haus Zu verkaufen ist.
Maße ca. 76 x 244cm
Es darf gerne frech und modern sein mit einem witzigen einladenden Spruch sein, sollte aber auch ansonsten zu meinem chicen Style passen (siehe Homepage www.kranichhausverkauf.de) es soll sich abheben von anderen langweiligen Bannern.
Ggf soll die Plane auch noch an einem Tennisplatz angebracht werden

```html
<!DOCTYPE html>
<html lang="de">
<head>
<meta charset="utf-8">
<title>Banner – Kranich Immobilien</title>
<link href="https://fonts.googleapis.com/css2?family=Roboto:wght@400;700;900&display=swap" rel="stylesheet">
<style>
  :root {
    --page-bg: #e6e6e7;
    --ink: #1f1f1f;
    --bar: #2b2b2b;
    --gold: #c9a45e;
    --gold-light: #e8d8b4;
    --cream: #f3ece0;
    --white: #ffffff;
  }
  * { margin: 0; padding: 0; box-sizing: border-box; }
  html, body {
    width: 1200px; height: 720px; overflow: hidden;
    background: var(--page-bg);
    font-family: "Roboto", Arial, sans-serif;
  }
  .banner {
    position: absolute; left: 30px; top: 170px;
    width: 1140px; height: 379px;
    overflow: hidden;
    background: linear-gradient(100deg, var(--cream) 0%, var(--gold-light) 45%, #d9c089 70%, var(--cream) 100%);
    box-shadow: 0 10px 24px rgba(0,0,0,.12);
  }
  .banner__art { position: absolute; inset: 0; }
  .headline {
    position: absolute; color: var(--ink); line-height: 1; white-space: nowrap;
  }
  .headline--intro { left: 486px; top: 52px; font-size: 58px; font-weight: 400; letter-spacing: -0.5px; }
  .headline--main { left: 530px; top: 118px; font-size: 61px; font-weight: 900; letter-spacing: -0.5px; }
  .sale-strip {
    position: absolute; left: 391px; top: 197px;
    font-size: 34px; font-weight: 400; color: var(--white); white-space: nowrap; line-height: 1;
  }
  .sale-strip strong { color: var(--gold); font-weight: 700; }
  .contact {
    position: absolute; top: 302px; left: 0; right: 0; height: 77px;
    color: var(--white);
  }
  .contact__item {
    position: absolute; top: 0; height: 77px;
    display: flex; align-items: center; gap: 10px; white-space: nowrap;
  }
  .contact__item svg { flex: none; }
  .contact__item--phone { left: 30px; font-size: 29px; font-weight: 700; }
  .contact__item--mail { left: 372px; font-size: 21px; font-weight: 700; }
  .contact__item--web { left: 706px; font-size: 21px; font-weight: 700; }
  .brand {
    position: absolute; left: 1017px; top: 262px;
    width: 92px; height: 92px; border-radius: 50%;
    background: var(--bar); border: 2px solid var(--gold-light);
    display: flex; align-items: center; justify-content: center; text-align: center;
    color: var(--white); font-size: 12px; font-weight: 700; line-height: 1.25;
  }
</style>
</head>
<body>
  <div class="banner">
    <svg class="banner__art" width="1140" height="379" viewBox="0 0 1140 379">
      <defs>
        <linearGradient id="photoTone" x1="0" y1="0" x2="1" y2="1">
          <stop offset="0" stop-color="#c9ced3"/>
          <stop offset="0.5" stop-color="#8a8f94"/>
          <stop offset="1" stop-color="#6e4a38"/>
        </linearGradient>
      </defs>
      <polygon points="0,0 455,0 286,302 0,302" fill="url(#photoTone)" role="img" aria-label="Foto: glückliche Familie spielt im hellen Wohnzimmer"/>
      <polygon points="346,191 1117,191 1117,241 330,241" fill="var(--bar)"/>
      <rect x="0" y="302" width="1140" height="77" fill="var(--bar)"/>
    </svg>

    <div class="headline headline--intro">Lust auf einen</div>
    <div class="headline headline--main">TAPETENWECHSEL?</div>
    <div class="sale-strip">DIESE IMMOBILIE STEHT <strong>ZUM VERKAUF!</strong></div>

    <div class="contact">
      <div class="contact__item contact__item--phone">
        <svg width="26" height="26" viewBox="0 0 24 24"><path fill="var(--gold)" d="M6.6 10.8a15.1 15.1 0 0 0 6.6 6.6l2.2-2.2c.3-.3.7-.4 1-.2 1.1.4 2.3.6 3.6.6.6 0 1 .4 1 1V20c0 .6-.4 1-1 1A17 17 0 0 1 3 4c0-.6.4-1 1-1h3.5c.6 0 1 .4 1 1 0 1.3.2 2.5.6 3.6.1.3 0 .7-.2 1z"/></svg>
        <span>01234 / 56 78 900</span>
      </div>
      <div class="contact__item contact__item--mail">
        <svg width="26" height="18" viewBox="0 0 26 18"><rect width="26" height="18" fill="var(--gold)"/><path d="M0 0 13 10 26 0" fill="none" stroke="var(--bar)" stroke-width="2"/></svg>
        <span>info@kranichhausverkauf.de</span>
      </div>
      <div class="contact__item contact__item--web">
        <svg width="26" height="26" viewBox="0 0 26 26" fill="none" stroke="var(--gold)" stroke-width="2"><circle cx="13" cy="13" r="11"/><ellipse cx="13" cy="13" rx="5" ry="11"/><path d="M2 13h22M4 7h18M4 19h18"/></svg>
        <span>www.kranichhausverkauf.de</span>
      </div>
    </div>

    <div class="brand">Kranich<br>Immobilien</div>
  </div>
</body>
</html>
```